Business cards for Brightmarrow Consulting with the following info for the front side:

Brightmarrow Consulting
Executive Coaching and Human Capital Strategy
www.brightmarrow.example

Lorena Vaduvic
Principal
lorena@brightmarrow.example
+1 604 555 0172

Black background, text using the colours of the logo - enclosed.

The back side of the business card should feature the logo in the middle, with "Executive Coaching and Human Capital Strategy" on top and "www.brightmarrow.example" below.

```html
<!DOCTYPE html>
<html lang="en">
<head>
<meta charset="utf-8">
<title>Brightmarrow Consulting — Business Cards</title>
<link rel="stylesheet" href="https://fonts.googleapis.com/css2?family=Open+Sans:wght@400;600&display=swap">
<style>
  :root {
    --stage: #1b1d1c;
    --card: #1e1e21;
    --card-light: #2a2a2e;
    --blue: #2a9fd8;
    --gold: #e8a317;
    --white: #f2f2f4;
    --silver: #d6d7dc;
  }
  * { box-sizing: border-box; margin: 0; padding: 0; }
  html, body {
    width: 1200px; height: 800px; overflow: hidden;
    background: var(--stage);
    font-family: "Open Sans", Arial, sans-serif;
  }
  .canvas {
    position: relative; width: 1200px; height: 800px;
    display: flex; align-items: center; justify-content: center; gap: 40px;
  }
  .card {
    position: relative; width: 540px; height: 310px;
    background: linear-gradient(135deg, var(--card) 0%, var(--card) 45%, var(--card-light) 100%);
    box-shadow: 0 12px 30px rgba(0,0,0,.45);
  }

  /* Front */
  .holder { position: absolute; left: 34px; top: 38px; }
  .holder-name { color: var(--blue); font-weight: 600; font-size: 22px; letter-spacing: .3px; line-height: 1.1; }
  .holder-role { color: var(--gold); font-weight: 600; font-size: 11px; margin-top: 2px; }
  .holder-rule { position: absolute; left: 14px; top: 92px; width: 210px; height: 1.5px; background: var(--white); }

  .brand { position: absolute; right: 36px; top: 128px; display: flex; align-items: center; gap: 10px; }
  .brand-mark { width: 44px; height: 44px; border: 2px solid var(--gold); border-radius: 50%; }
  .brand-name { color: var(--blue); font-weight: 600; font-size: 30px; letter-spacing: 1.5px; }

  .contact { position: absolute; left: 42px; top: 206px; padding-left: 20px; border-left: 1.5px solid var(--white); }
  .contact-company { color: var(--blue); font-weight: 600; font-size: 13px; margin-bottom: 7px; }
  .contact-line { display: flex; align-items: center; gap: 9px; color: var(--gold); font-weight: 600; font-size: 11.5px; line-height: 20px; }
  .contact-line svg { width: 13px; height: 13px; flex: none; }

  /* Back */
  .card-back { display: flex; flex-direction: column; align-items: center; }
  .tagline { color: var(--white); font-weight: 600; font-size: 15px; margin-top: 40px; }
  .emblem {
    margin-top: 22px; width: 140px; height: 140px; border-radius: 50%;
    border: 3px solid var(--silver);
    display: flex; align-items: center; justify-content: center;
  }
  .emblem-name { color: var(--silver); font-weight: 600; font-size: 15px; letter-spacing: 1px; }
  .web { color: var(--silver); font-weight: 600; font-size: 13px; letter-spacing: 3px; margin-top: 22px; }
</style>
</head>
<body>
<main class="canvas">
  <section class="card card-front">
    <div class="holder">
      <p class="holder-name">Lorena Vaduvic</p>
      <p class="holder-role">Principal</p>
    </div>
    <div class="holder-rule"></div>

    <div class="brand">
      <span class="brand-mark"></span>
      <span class="brand-name">BRIGHTMARROW</span>
    </div>

    <div class="contact">
      <p class="contact-company">Brightmarrow Consulting</p>
      <p class="contact-line">
        <svg viewBox="0 0 16 16" fill="none" stroke="#2a9fd8" stroke-width="1.3" aria-hidden="true"><path d="M3 1.5l3 3-1.6 1.8a9 9 0 0 0 5.3 5.3L11.5 10l3 3-2 2C6.5 14.5 1.5 9.5 1 3.5z"/></svg>
        +1 604 555 0172
      </p>
      <p class="contact-line">
        <svg viewBox="0 0 16 16" fill="none" stroke="#2a9fd8" stroke-width="1.3" aria-hidden="true"><rect x="1" y="3.5" width="14" height="9"/><path d="M1 3.5l7 5.5 7-5.5"/></svg>
        lorena@brightmarrow.example
      </p>
      <p class="contact-line">
        <svg viewBox="0 0 16 16" fill="none" stroke="#2a9fd8" stroke-width="1.2" aria-hidden="true"><circle cx="8" cy="8" r="6.5"/><ellipse cx="8" cy="8" rx="3" ry="6.5"/><path d="M1.5 8h13M2.5 4.8h11M2.5 11.2h11"/></svg>
        www.brightmarrow.example
      </p>
    </div>
  </section>

  <section class="card card-back">
    <p class="tagline">Executive Coaching and Human Capital Strategy</p>
    <div class="emblem"><span class="emblem-name">BRIGHTMARROW</span></div>
    <p class="web">www.brightmarrow.example</p>
  </section>
</main>
</body>
</html>
```